Business card design needed

Chasing a very simplistic modern design with a logo incorporating "TRV".
I'm starting a plumbing business.
I do water, sanitary and drainage plumbing that will cover residential, commercial, rental, rural, excavation, new housing and all maintanence requirements.

Industry/Entity Type

Business

Contact Information for Business Card

TRV PLUMBING SERVICES
DEAN HOLLOWBY - LICENSED PLUMBER
PHONE: 0481926574
E-MAIL: hollodt7@wirelane.com
NORTHERN SUBURBS

Requirements
Must have
• lower case email address

```html
<!DOCTYPE html>
<html lang="en">
<head>
<meta charset="utf-8">
<title>TRV Plumbing Services – Business Card</title>
<link rel="stylesheet" href="https://fonts.googleapis.com/css2?family=Advent+Pro:wght@500;600&display=swap">
<style>
  :root {
    --backdrop: #ececec;
    --card-white: #ffffff;
    --brand-blue: #2249e6;
    --brand-blue-deep: #1b35ad;
    --text-white: #ffffff;
  }
  html, body {
    margin: 0;
    padding: 0;
    width: 1200px;
    height: 741px;
    overflow: hidden;
    background: var(--backdrop);
  }
  .canvas {
    position: relative;
    width: 1200px;
    height: 741px;
  }
  .card {
    position: absolute;
    left: 60px;
    top: 60px;
    width: 1080px;
    height: 620px;
    background: var(--card-white);
    overflow: hidden;
    font-family: "Advent Pro", "Arial Narrow", sans-serif;
    box-shadow: 0 6px 18px rgba(0,0,0,0.18);
  }
  .wave {
    position: absolute;
    inset: 0;
    width: 1080px;
    height: 620px;
  }
  .holder-name {
    position: absolute;
    left: 42px;
    top: 30px;
    margin: 0;
    font-size: 104px;
    font-weight: 600;
    letter-spacing: 3px;
    line-height: 1;
    color: var(--brand-blue);
  }
  .brand-mark {
    position: absolute;
    right: 34px;
    top: 176px;
    margin: 0;
    font-size: 250px;
    font-weight: 600;
    line-height: 1;
    letter-spacing: -4px;
    color: var(--brand-blue);
  }
  .brand-tagline {
    position: absolute;
    right: 34px;
    top: 426px;
    margin: 0;
    font-size: 40px;
    font-weight: 600;
    letter-spacing: 1px;
    color: var(--text-white);
  }
  .contact-list {
    position: absolute;
    left: 42px;
    top: 414px;
    margin: 0;
    padding: 0;
    list-style: none;
    font-size: 38px;
    font-weight: 600;
    letter-spacing: 1px;
    color: var(--text-white);
  }
  .contact-list li {
    height: 60px;
    line-height: 56px;
  }
</style>
</head>
<body>
<div class="canvas">
  <article class="card">
    <svg class="wave" viewBox="0 0 1080 620" aria-hidden="true">
      <defs>
        <linearGradient id="bandFill" x1="0" y1="0" x2="1" y2="0">
          <stop offset="0" stop-color="var(--brand-blue)" style="stop-color:#2249e6"/>
          <stop offset="1" stop-color="var(--brand-blue-deep)" style="stop-color:#1b35ad"/>
        </linearGradient>
      </defs>
      <path d="M0,384 C150,350 330,338 530,362 S900,412 1080,392 L1080,620 L0,620 Z" fill="url(#bandFill)"/>
    </svg>

    <h1 class="holder-name">DEAN HOLLOWBY</h1>

    <p class="brand-mark">TRV</p>
    <p class="brand-tagline">PLUMBING SERVICES</p>

    <ul class="contact-list">
      <li>CALL: 0481926574</li>
      <li>MAILTO: hollodt7@wirelane.com</li>
      <li>NORTHERN SUBURBS</li>
    </ul>
  </article>
</div>
</body>
</html>
```